Business Card Design Project

Business Card
We are rebranding with a new logo
Industry/Entity Type
Business
Contact Information for Business Card
Dennis Marlow +61 427581962 dennis@qovo.com.au P.O. Box 872 Kelvindale QLD 4309
Requirements
Must have
- Logo

```html
<!DOCTYPE html>
<html lang="en">
<head>
<meta charset="utf-8">
<title>Qovo International – Business Card</title>
<link href="https://fonts.googleapis.com/css2?family=Lato:wght@400;700;900&display=swap" rel="stylesheet">
<style>
  :root {
    --backdrop: #c8c8c8;
    --card: #ffffff;
    --ink: #111111;
    --brand-blue: #1a7fb8;
    --icon-blue: #5bbde8;
    --band-orange: #f28a22;
  }
  * { box-sizing: border-box; margin: 0; padding: 0; }
  html, body {
    width: 1200px; height: 1000px; overflow: hidden;
    background: var(--backdrop);
    font-family: "Lato", Arial, sans-serif;
  }
  .business-card {
    position: absolute; left: 120px; top: 226px;
    width: 960px; height: 548px;
    background: var(--card);
    box-shadow: 4px 6px 8px rgba(0,0,0,0.35);
    overflow: hidden;
  }
  .brand {
    position: absolute; left: 112px; top: 248px;
    display: flex; align-items: center; gap: 14px;
  }
  .brand-dot {
    width: 30px; height: 30px; border-radius: 50%;
    background: var(--brand-blue);
  }
  .brand-name {
    font-weight: 700; font-size: 34px; color: var(--brand-blue);
    letter-spacing: 0.5px;
  }
  .contact-line {
    position: absolute; left: 580px;
    display: flex; align-items: flex-start; gap: 18px;
    font-weight: 700; font-size: 22px; color: var(--ink);
    letter-spacing: 1px; line-height: 34px;
  }
  .contact-line svg { flex: none; margin-top: 5px; }
  .contact-phone { top: 66px; }
  .contact-email { top: 124px; }
  .contact-address { top: 396px; }
  .name-band {
    position: absolute; left: 538px; top: 179px;
    width: 422px; height: 177px;
    background: var(--band-orange);
    border-radius: 8px 0 0 8px;
  }
  .person-name {
    position: absolute; left: 38px; top: 0; height: 100%;
    display: flex; align-items: center;
    font-size: 35px; color: #ffffff; font-weight: 400; letter-spacing: 1px;
  }
  .person-name strong { font-weight: 900; margin-right: 10px; }
</style>
</head>
<body>
  <main class="business-card">
    <div class="brand">
      <span class="brand-dot"></span>
      <span class="brand-name">Qovo International</span>
    </div>

    <div class="contact-line contact-phone">
      <svg width="24" height="24" viewBox="0 0 24 24" aria-hidden="true">
        <circle cx="12" cy="12" r="12" fill="var(--icon-blue)"/>
        <path d="M8.2 6.5c.5-.3 1.1-.2 1.4.3l1 1.7c.3.5.2 1-.2 1.3l-.7.5c.6 1.4 1.6 2.5 3 3.1l.5-.7c.3-.4.9-.5 1.3-.2l1.7 1c.5.3.6.9.3 1.4l-.6.9c-.4.6-1.2.9-1.900.6-3.2-1.2-5.6-3.6-6.8-6.8-.3-.7 0-1.5.6-1.9z" fill="#fff"/>
      </svg>
      <span>+61 427581962</span>
    </div>

    <div class="contact-line contact-email">
      <svg width="24" height="24" viewBox="0 0 24 24" aria-hidden="true">
        <circle cx="12" cy="12" r="12" fill="var(--icon-blue)"/>
        <rect x="6" y="8" width="12" height="8.5" rx="1" fill="#fff"/>
        <path d="M6.5 8.6l5.5 4 5.5-4" fill="none" stroke="var(--icon-blue)" stroke-width="1.2"/>
      </svg>
      <span>dennis@qovo.com.au</span>
    </div>

    <div class="name-band">
      <div class="person-name"><strong>Dennis</strong>Marlow</div>
    </div>

    <div class="contact-line contact-address">
      <svg width="24" height="24" viewBox="0 0 24 24" aria-hidden="true">
        <circle cx="12" cy="12" r="12" fill="var(--icon-blue)"/>
        <g fill="none" stroke="#fff" stroke-width="1.1">
          <circle cx="12" cy="12" r="6"/>
          <ellipse cx="12" cy="12" rx="2.6" ry="6"/>
          <path d="M6 12h12M7 9h10M7 15h10"/>
        </g>
      </svg>
      <span>P.O. Box 872<br>Kelvindale QLD 4309</span>
    </div>
  </main>
</body>
</html>
```